Q.R. Bright Desk Store

The design is for eCommerce home page but I would like it to complement this site: http://www.qrbrightdesksystems.com/ but... it should also have independence as a standalone site.

The best design will be able to effectively mix corporate with a high quality small business consumer feel. It should be completely custom design, not a template look or feel. I want the users to get the feeling that this is the place to go for buying tech for business. We sell the same products as Vantrel.

You can be creative as you wish, as long as the elements of a great eCommerce site are present.

I would like your 'design' to blow these away:
http://www.buying.zorvex.com/
mivoland.com
http://www.vantrel.com/

Here are references:
Call to action
http://trabelwise.com/us/blog/48173-seven-tips-for-designing-an-effective-ecommerce-call-to-action

Effective Ecommerce design
http://www.plov.com/ss/7-tips-for-effective-e-commerce#0

91 points of ecommerce
http://dreb.com/blog/holygrail-of-ecommerce-conversion-optimization-91-points-checklist

UPDATE 07/11/2013:

Please look at the category sample png files. I see already many people are using the main menu from qrbrightdesksystems.com and I do not mind your creativiety, but this is an eCommerce store and people need a menu to get to the categories and/or product types. I don't want to limit anyone creativity by the png samples. I'm also not using them to show I like them in any particular way or form, just that it's needed, whether it's a button (dropdown of course) that says 'Categories' or 'Products, whether it an accordion, horizontal or vertical.

Thanks

UPDATE 07/12/2013:

Please find other use of space that has been used for About Us paragraph (if you've added it to the page). About Us should have it's own page and the purpose of the design should be to sell products (and some services as products). Please put a link or some other creative method to lead users to the About Us page.

Reason: I've raised the award, including 1st, 2nd, and 3rd place and participation payments so I will also extend 7 days. Thanks!

I've updated the product brief. Please scroll down to where it says: UPDATE 07/11/2013

Thanks!

UPDATE 07/12/2013:

Please find other use of space that has been used for About Us paragraph (if you've added it to the page).  About Us should have it's own page and the purpose of the design should be to sell products (and some services as products). Please put a link or some other creative method to lead users to the About Us page if you must but not on the real estate of the page.

Thanks!

Added updates to the brief 7/14/2013.

Thanks!

The voting is in and the project is complete.  Thanks everyone for joining, all of those who participated are truly amazingly talented. But, there were only 3 prizes.  I will be having further projects down the line to develop other pages to this site after the initial implementation is completed.  I truly would like to have you all back. 

- Thank you.

Target Market(s)

corporate decision-makers AND small business consumers

Industry/Entity Type

Small Business

Requirements
Must have
• Call to action.
Openness (non-clutter).

These elements:
Search box
Logo
Tagline
Telephone number
Contact details
Address
My account / sign in
Shopping basket / checkout link
Latest offers
Promotional area
Email sign up
Delivery information
About us
Link to press office / corporate site
Terms and conditions
Sitemap for the footer.
Delivery offers: free
Personalized recommendations
Social media links
Accepted payment methods
Link to blog or community section
Change language / country

http://freshnotesblog.kelvarant.com/sales-leads-landing-page/

UPDATE 07/14/2013
Category Menu. This can be a dropdown, horizontal, vertical, etc. But shoppers need to know how to get to the products they want to buy.
Nice to have
• Trustmarks
Blog/Blog link

UPDATE 07/12/2013:
Make the footer useful.

UPDATE 07/14/2013 (Suggestions of elements to differentiate your designs)

-Quick Shop: A quick buy module/section: Where a user can put in a SKU number or Model number to quickly add the product to their shopping cart.

-Featured
-Best Sellers
-Specials
-Trending Tags/Tag Cloud
- Activity Stream
- Cross Sell/ Up Sell
- Testimonial
- Social Network Feed
- Live Help
- Feedback/Support/Contact Tab
- Show logged in user (i.e. Welcome, Mark Pell)
Should not have
• The design SHOULD NOT be generic like this:

http://www.artflock.com/design/52392
http://www.pelicanvault.com/

The page should not feel over cluttered. It should not have low quality icons or design elements. Navigation should not be hard to discover or confusing.

```html
<!DOCTYPE html>
<html lang="en">
<head>
<meta charset="utf-8">
<title>Q.R. Bright Desk Store</title>
<link rel="stylesheet" href="https://fonts.googleapis.com/css2?family=Exo+2:wght@400;600;800&family=Open+Sans:wght@400;600;700&display=swap">
<style>
:root{
  --navy:#0a3a82;
  --blue:#1c6fc4;
  --sky:#5bb2e8;
  --pale:#e9f2fb;
  --ink:#1d1d1d;
  --grey:#7a7a7a;
  --line:#d6d6d6;
  --panel:#eeeeee;
  --foot:#4a4a4a;
  --foot-ink:#c9c9c9;
  --green:#2fa84f;
}
*{box-sizing:border-box;margin:0;padding:0}
html,body{width:754px;height:1200px;overflow:hidden}
body{position:relative;background:radial-gradient(ellipse at 50% 30%,#fff 0,#f3f3f3 70%);font-family:"Open Sans",sans-serif;color:var(--ink);font-size:8px}
.abs{position:absolute}
a{color:inherit;text-decoration:none}
.lang{left:112px;top:9px;color:var(--blue)}
.lang b{color:var(--ink);font-weight:400}
.account{right:106px;top:9px;color:var(--blue)}
.account span{color:var(--ink)}
.utility{left:110px;top:36px;display:flex;gap:15px;color:#555;font-size:7.5px}
.search{left:458px;top:33px;width:98px;height:17px;background:var(--blue)}
.search-btn{left:558px;top:34px}
.icon{width:20px;height:20px;border-radius:50%;background:var(--navy);border:2px solid #fff;box-shadow:0 0 0 1px var(--navy)}
.rule{left:108px;width:540px;border-top:1px dashed var(--line)}
.logo{left:108px;top:58px;display:flex;align-items:center;gap:6px}
.logo-mark{width:36px;height:36px;border-radius:50%;background:var(--navy)}
.logo-name{font-family:"Exo 2",sans-serif;font-size:19px;font-weight:400;color:var(--blue);letter-spacing:.5px}
.mainnav{top:76px;display:flex;flex-direction:column}
.mainnav b{font-family:"Exo 2",sans-serif;font-weight:600;font-size:11.5px;color:var(--navy);letter-spacing:-.3px}
.mainnav i{font-style:normal;font-size:6.5px;color:var(--blue);letter-spacing:.3px}
.hero-img{left:108px;top:138px;width:272px;height:268px;border-radius:8px;background:radial-gradient(ellipse at 45% 45%,#3c3c3c 0,#1a1a1a 45%,#d8d8d8 100%)}
.deal{left:396px;top:203px}
.deal h1{font-family:"Exo 2",sans-serif;font-weight:800;font-size:25px;color:var(--navy);letter-spacing:-1px;line-height:1}
.deal h2{font-family:"Exo 2",sans-serif;font-weight:600;font-size:14px;color:var(--blue);line-height:1.1}
.deal ul{list-style:none;margin-top:10px}
.deal li{font-size:10px;font-weight:600;color:var(--blue);display:flex;align-items:center;gap:6px;margin-bottom:6px}
.deal li::before{content:"";width:7px;height:7px;border-radius:50%;border:3px solid var(--blue);background:#fff}
.cta{left:396px;top:296px;width:157px;height:34px;border-radius:5px;background:linear-gradient(#2d7fd0,var(--navy));color:#fff;font-family:"Exo 2",sans-serif;font-weight:800;font-size:17px;display:flex;align-items:center;justify-content:center;letter-spacing:-.5px}
.card{top:438px;height:128px;background:#fff;box-shadow:0 2px 4px rgba(0,0,0,.15);padding:6px 7px}
.card h3{font-family:"Exo 2",sans-serif;font-weight:600;font-size:17px;color:var(--sky);border-bottom:1px dashed #aac9e4;padding-bottom:2px;letter-spacing:-.3px}
.card .ph{height:60px;margin:8px 0 6px;border-radius:3px}
.card p{font-size:7px;color:var(--grey);line-height:1.35}
.pct{left:216px;top:479px;font-family:"Exo 2",sans-serif;font-weight:800;font-size:28px;color:var(--navy)}
.pct-price{left:221px;top:512px;font-family:"Exo 2",sans-serif;font-weight:600;font-size:12px;color:var(--sky)}
.quick{left:108px;top:584px;width:540px;height:30px;background:var(--pale);border:1px solid #b8d4ee}
.quick h4{left:9px;top:7px;font-family:"Exo 2",sans-serif;font-weight:800;font-size:13px;color:var(--navy)}
.field{top:5px;width:139px;height:18px;background:#fff;border:1px solid #ccc;font-size:7.5px;padding:4px 8px;color:#333}
.add{left:428px;top:5px;width:94px;height:18px;background:var(--navy);color:#fff;font-weight:700;font-size:7.5px;display:flex;align-items:center;justify-content:center;gap:5px}
.side{left:108px;top:625px;width:98px}
.tab{height:15px;background:var(--navy);color:#fff;font-size:7px;font-weight:700;padding:3px 6px;margin-bottom:3px}
.tab.on{background:var(--sky)}
.side ul{list-style:none;padding:2px 6px 5px;border-left:1px solid var(--line);border-right:1px solid var(--line)}
.side li{font-size:7px;color:#555;padding:3px 0;border-bottom:1px dashed var(--line)}
.side li::before{content:"▸ ";font-size:6px}
.prods{left:212px;top:625px;width:436px;height:177px;background:#fff;border:1px solid var(--line)}
.prod{top:9px;width:120px}
.prod h5{font-family:"Exo 2",sans-serif;font-weight:800;font-size:10px;color:var(--ink)}
.prod .ph{height:92px;margin:8px 0 10px;border-radius:4px}
.prod p{font-size:7px;color:var(--grey);line-height:1.3}
.prod strong{display:block;font-family:"Exo 2",sans-serif;font-weight:800;font-size:13px;color:var(--navy);margin-top:3px}
.vsep{top:15px;height:150px;border-left:1px dashed var(--line)}
.strip{left:110px;top:814px;width:538px;height:70px;background:var(--panel);border:1px solid #ddd}
.strip h6{font-family:"Exo 2",sans-serif;font-weight:600;font-size:13px;color:var(--grey);top:9px;text-align:center;letter-spacing:-.3px}
.soc{width:16px;height:16px;border-radius:50%;background:var(--navy);top:35px}
.mail{left:190px;top:35px;width:125px;height:18px;background:#fff;border:1px solid #ccc;font-size:7px;padding:4px 8px}
.mail-go{left:316px;top:35px;width:20px;height:18px;background:var(--navy)}
.tt{left:370px;top:33px;font-family:"Exo 2",sans-serif;font-weight:800;font-size:15px;color:var(--navy);white-space:nowrap}
.tt small{font-size:7px}
.contact{left:448px;top:36px;font-size:6.5px;color:var(--sky);line-height:1.6;white-space:nowrap}
.testi-h{left:110px;top:905px;font-family:"Exo 2",sans-serif;font-weight:600;font-size:13px;color:var(--grey)}
.testi{top:928px;display:flex;gap:8px;width:160px}
.avatar{width:56px;height:56px;border-radius:50%;flex:none;background:linear-gradient(#e2e2e2,#9a9a9a)}
.testi p{font-size:6.2px;line-height:1.35;color:#333;padding-top:22px}
.testi em{display:block;font-style:normal;color:var(--green);margin-top:4px}
.footer{left:0;top:1018px;width:754px;height:182px;background:var(--foot)}
.fcol{top:1032px;color:var(--foot-ink)}
.fcol h6{font-family:"Exo 2",sans-serif;font-weight:600;font-size:9.5px;margin-bottom:6px;color:#d8d8d8}
.fcol a{display:block;font-size:7.3px;line-height:13.7px}
.fsep{top:1036px;height:90px;border-left:1px dashed #6a6a6a}
.fline{left:108px;top:1152px;width:540px;border-top:1px dashed #6a6a6a}
.copy{left:108px;top:1170px;font-size:7px;color:var(--foot-ink)}
.accept{left:327px;top:1167px;display:flex;align-items:center;gap:4px;color:#e8e8e8;font-family:"Exo 2",sans-serif;font-weight:600;font-size:10px}
.card-chip{width:16px;height:11px;background:#d0d0d0;border-radius:1px}
.flogo{left:551px;top:1160px;display:flex;align-items:center;gap:5px}
.flogo .logo-mark{width:26px;height:26px;background:#777}
.flogo span{font-family:"Exo 2",sans-serif;font-size:13px;color:#9a9a9a}
</style>
</head>
<body>
<div class="abs lang">Select Your Language: <b>English ▾</b></div>
<div class="abs account"><a>Sign In</a> <span>or</span> <a>Register</a></div>
<nav class="abs utility"><a>Home</a><a>Small Business</a><a>Enterprise</a><a>Non-Profit</a><a>Billing</a><a>Get Support</a><a>Contact Us</a></nav>
<div class="abs search"></div>
<svg class="abs search-btn" width="14" height="14" viewBox="0 0 14 14"><circle cx="5.5" cy="5.5" r="4" fill="none" stroke="#888" stroke-width="1.6"/><path d="M8.5 8.5l4 4" stroke="#888" stroke-width="2"/></svg>
<div class="abs icon" style="left:581px;top:31px"></div>
<div class="abs icon" style="left:604px;top:31px"></div>
<div class="abs icon" style="left:626px;top:31px"></div>
<div class="abs rule" style="top:55px"></div>
<div class="abs logo"><div class="logo-mark"></div><div class="logo-name">Q.R. Bright Desk</div></div>
<a class="abs mainnav" style="left:311px"><b>HARDWARE</b><i>FULFILLMENT</i></a>
<a class="abs mainnav" style="left:396px"><b>SOFTWARE</b><i>LICENSING</i></a>
<a class="abs mainnav" style="left:477px"><b>IT RESOURCE</b><i>MANAGEMENT</i></a>
<a class="abs mainnav" style="left:567px"><b>TECHNOLOGY</b><i>SERVICES</i></a>
<div class="abs rule" style="top:113px"></div>

<div class="abs hero-img" role="img" aria-label="Glossy black laptop opened at an angle"></div>
<div class="abs deal">
  <h1>DEAL OF THE WEEK</h1>
  <h2>MONDAY-FRIDAY ONLY</h2>
  <ul><li>Highly Mobile and Secure</li><li>Zorvex ProSlate 45</li></ul>
</div>
<a class="abs cta">CHECK IT OUT</a>

<div class="abs rule" style="top:436px"></div>
<section class="abs card" style="left:108px;width:176px"><h3>Latest Offers</h3><div class="ph" role="img" aria-label="Colour inkjet printer" style="width:95px;background:linear-gradient(#555,#1e1e1e)"></div><p>Lorem ipsum dolor sit amet, consectetuer adipiscing elit, sed diam nonummy nibh...</p></section>
<div class="abs pct">15%</div><div class="abs pct-price">$79.99</div>
<section class="abs card" style="left:291px;width:174px"><h3>Today Special</h3><div class="ph" role="img" aria-label="Digital camera with flip-out screen" style="width:110px;margin-left:25px;background:linear-gradient(#444,#111)"></div><p>Lorem ipsum dolor sit amet, consectetuer adipiscing elit, sed diam nonummy nibh...</p></section>
<section class="abs card" style="left:472px;width:176px"><h3>Best Sellers</h3><div class="ph" role="img" aria-label="Open hard disk drive" style="width:70px;margin-left:54px;background:linear-gradient(135deg,#ddd,#555)"></div><p>Lorem ipsum dolor sit amet, consectetuer adipiscing elit, sed diam nonummy nibh...</p></section>

<div class="abs quick">
  <h4 class="abs">QUICK SHOP</h4>
  <div class="abs field" style="left:114px">Enter SKU Number</div>
  <div class="abs field" style="left:259px">Enter Model Number</div>
  <div class="abs add"><svg width="9" height="9" viewBox="0 0 9 9"><path d="M1 3h7l-1 5H2z" fill="#fff"/><path d="M3 3a1.5 1.5 0 013 0" stroke="#fff" fill="none"/></svg>ADD TO CART</div>
</div>

<aside class="abs side">
  <div class="tab">WAYS TO SHOP</div>
  <div class="tab on">FEATURED</div>
  <ul><li>Fortivane</li><li>Netmoor</li><li>Dark Plum</li><li>Kestrel Lab</li></ul>
  <div class="tab" style="margin-top:4px">NOTEBOOKS</div>
  <div class="tab">DESKTOPS</div>
  <div class="tab">DATA STORAGE</div>
  <div class="tab">PRINTERS</div>
</aside>
<section class="abs prods">
  <div class="abs prod" style="left:13px"><h5>PRODUCT 01</h5><div class="ph" role="img" aria-label="White head-mounted video viewer" style="width:80px;margin-left:10px;background:linear-gradient(#f4f4f4,#9a9a9a)"></div><p>Lorem ipsum dolor sit amet, consectetuer adipiscing...</p><strong>$79.99</strong></div>
  <div class="abs vsep" style="left:147px"></div>
  <div class="abs prod" style="left:160px"><h5 style="margin-left:-10px">PRODUCT 02</h5><div class="ph" role="img" aria-label="Laptop showing a tiled start screen" style="width:120px;background:linear-gradient(#3a5fa8,#c0c4cc)"></div><p>Lorem ipsum dolor sit amet, consectetuer adipiscing...</p><strong>$235.99</strong></div>
  <div class="abs vsep" style="left:296px"></div>
  <div class="abs prod" style="left:315px"><h5 style="margin-left:-6px">PRODUCT 03</h5><div class="ph" role="img" aria-label="White office projector" style="width:110px;background:linear-gradient(#fafafa,#b5b5b5)"></div><p>Lorem ipsum dolor sit amet, consectetuer adipiscing...</p><strong>$130.99</strong></div>
</section>

<section class="abs strip">
  <h6 class="abs" style="left:0;width:168px">WE ARE SOCIAL</h6>
  <div class="abs soc" style="left:43px"></div><div class="abs soc" style="left:62px"></div><div class="abs soc" style="left:81px"></div><div class="abs soc" style="left:100px"></div>
  <div class="abs" style="left:168px;top:8px;height:54px;border-left:1px solid #d0d0d0"></div>
  <h6 class="abs" style="left:168px;width:190px">NEWSLETTER</h6>
  <div class="abs mail">Enter Your Email Address</div>
  <div class="abs mail-go"><svg width="20" height="18" viewBox="0 0 20 18"><path d="M8 5l5 4-5 4z" fill="#fff"/></svg></div>
  <div class="abs" style="left:358px;top:8px;height:54px;border-left:1px solid #d0d0d0"></div>
  <h6 class="abs" style="left:358px;width:180px">LIVE HELP</h6>
  <div class="abs tt">24/7 <small>SUPPORT</small></div>
  <div class="abs contact">
    <div><svg width="8" height="8" viewBox="0 0 8 8"><path d="M1 1l2 0 1 2-1 1a4 4 0 002 2l1-1 2 1v2C4 8 0 4 1 1z" fill="#5bb2e8"/></svg> +1 (888) 555 0142</div>
    <div><svg width="8" height="6" viewBox="0 0 8 6"><rect width="8" height="6" fill="#5bb2e8"/><path d="M0 0l4 3 4-3" stroke="#fff" fill="none"/></svg> info@qrbrightdeskinc.com</div>
  </div>
</section>
<div class="abs rule" style="top:894px"></div>

<h2 class="abs testi-h">TESTIMONIALS</h2>
<div class="abs testi" style="left:110px"><div class="avatar" role="img" aria-label="Portrait of a smiling customer in a suit"></div><p>Lorem ipsum dolor sit amet.Consectetuer adipiscing elit. Praesent vestibulum molestie lacus. Aenean nonummy hendrerit mauris.<em>Owen Lark</em></p></div>
<div class="abs" style="left:293px;top:930px;height:66px;border-left:1px dashed var(--line)"></div>
<div class="abs testi" style="left:302px"><div class="avatar" role="img" aria-label="Portrait of a customer in a suit and tie"></div><p>Lorem ipsum dolor sit amet.Consectetuer adipiscing elit. Praesent vestibulum molestie lacus. Aenean nonummy hendrerit mauris.<em>Ray Tobin</em></p></div>
<div class="abs" style="left:477px;top:930px;height:66px;border-left:1px dashed var(--line)"></div>
<div class="abs testi" style="left:486px"><div class="avatar" role="img" aria-label="Portrait of a customer with long dark hair"></div><p>Lorem ipsum dolor sit amet.Consectetuer adipiscing elit. Praesent vestibulum molestie lacus. Aenean nonummy hendrerit mauris.<em>Nina Falwe</em></p></div>

<footer class="abs footer"></footer>
<div class="abs fcol" style="left:111px"><h6>OUR COMPANY</h6><a>About Us</a><a>Careers</a><a>Corporate</a><a>Partners</a><a>Get Support</a><a>Contact Us</a></div>
<div class="abs fsep" style="left:214px"></div>
<div class="abs fcol" style="left:245px"><h6>QUICK LINKS</h6><a>Home</a><a>Small Business</a><a>Enterprise</a><a>Non-Profit</a><a>Billing</a><a>Go Shopping</a></div>
<div class="abs fsep" style="left:340px"></div>
<div class="abs fcol" style="left:367px"><h6>OUR WEBSITES</h6><a>qrbrightdeskstore.com</a><a>qrbrightdeskinc.com</a><a>qrbrightdesksupport.com</a><a>qrbrightdeskeducation</a></div>
<div class="abs fsep" style="left:478px"></div>
<div class="abs fcol" style="left:508px"><h6>PRODUCTS AND SERVICES</h6><a>Hardware Fulfillment</a><a>Software Licensing</a><a>Resource Management</a><a>Technical Services</a><a>Exchange Board</a><a>Partner Program</a><a>Recycle</a></div>
<div class="abs fline"></div>
<div class="abs copy">Copyright © 2013 Q.R. Bright Desk Store.</div>
<div class="abs accept">We Accept <span style="margin-left:4px">PayWell</span><span class="card-chip"></span><span class="card-chip"></span><span class="card-chip"></span></div>
<div class="abs flogo"><div class="logo-mark"></div><span>Q.R. Bright Desk</span></div>
</body>
</html>
```